Podiatry Clinic needs an A0 poster design

we need an A0 poster design for our clinic frontage to include our logo and a feet theme. it is located either in a frame on a glass wall, or in a freestanding poster holder within a shopping centre.
Our clinic values are integrity, respect, excellence, happiness and fun.
We want to let people know that if your feet fail you, then the rest of you slows down very quickly, so get your feet checked immediately. we deal with kids feet, sporty feet, mature feet.

Target Market(s)

parents with kids

Industry/Entity Type

Medical

Requirements
Must have
• Marlow Stride Clinic Logo
• www.marlowstrideclinic.net
• 7261 8092
• easy to read from a distance
Nice to have
• fun, friendly, inviting, colourful, happy.
Should not have
• cartoon
• ugly
• sad
• not too much text
• no fanciful fonts

```html
<!DOCTYPE html>
<html lang="en">
<head>
<meta charset="utf-8">
<title>Marlow Stride Clinic – Poster</title>
<link rel="stylesheet" href="https://fonts.googleapis.com/css2?family=Raleway:wght@400;500;600;700&display=swap">
<style>
  :root {
    --page-bg: #e9ecef;
    --paper: #ffffff;
    --brand-blue: #1f7cc4;
    --sky-blue: #3fa6df;
    --band-blue: #2a7fc6;
    --ink-blue: #1d6fb3;
    --warm-orange: #e9a23b;
    --skin-pink: #c99a92;
    --skin-light: #ead8d2;
    --sand: #efe3dc;
    --grass: #5f9a2e;
    --sky: #cfe4ef;
    --shirt-green: #7fbf3a;
    --shirt-red: #c42a2f;
    --shirt-yellow: #f2d532;
    --white: #ffffff;
  }
  * { box-sizing: border-box; margin: 0; padding: 0; }
  html, body {
    width: 1200px; height: 800px; overflow: hidden;
    background: var(--page-bg);
    font-family: "Raleway", Arial, sans-serif;
  }
  .poster {
    position: absolute; left: 340px; top: 32px;
    width: 520px; height: 736px;
    background: var(--paper);
    box-shadow: 0 6px 24px rgba(0,0,0,.15);
    display: flex; flex-direction: column;
  }
  .poster-header {
    height: 93px; display: flex; align-items: center;
    padding: 0 12px 0 14px; gap: 10px;
  }
  .brand { display: flex; align-items: center; gap: 8px; }
  .brand-mark {
    width: 40px; height: 40px; border-radius: 50%;
    background: var(--brand-blue); flex: none;
  }
  .brand-name {
    font-weight: 500; font-size: 20px; color: var(--brand-blue);
    white-space: nowrap;
  }
  .tagline {
    margin-left: auto; font-weight: 600; font-size: 15.5px;
    color: var(--brand-blue); line-height: 1.2; white-space: nowrap;
  }
  .feature { position: relative; height: 292px; overflow: hidden; }
  .feature svg, .kids svg { position: absolute; inset: 0; width: 100%; height: 100%; }
  .feature-copy {
    position: absolute; right: 6px; bottom: 14px; width: 250px;
    color: var(--white);
  }
  .feature-title { font-weight: 600; font-size: 29px; text-align: right; letter-spacing: .2px; }
  .feature-text {
    margin-top: 6px; font-size: 12.5px; line-height: 1.3;
    text-align: center; padding-left: 10px;
  }
  .divider { height: 17px; background: var(--band-blue); }
  .kids { position: relative; height: 262px; overflow: hidden; }
  .kids-copy {
    position: absolute; left: 8px; top: 166px; color: var(--white);
    font-weight: 600; font-size: 17px; line-height: 1.3;
  }
  .contact {
    flex: 1; display: flex; align-items: center; justify-content: space-between;
    padding: 0 12px;
  }
  .contact-item {
    display: flex; align-items: center; gap: 7px;
    font-weight: 600; font-size: 12.5px; color: var(--ink-blue);
  }
  .contact-item svg { flex: none; }
</style>
</head>
<body>
  <main class="poster">
    <header class="poster-header">
      <div class="brand">
        <span class="brand-mark"></span>
        <span class="brand-name">Marlow Stride Clinic</span>
      </div>
      <p class="tagline">"The greatest gifts in life<br>are those we give to others"</p>
    </header>

    <section class="feature">
      <svg viewBox="0 0 520 292" preserveAspectRatio="none" role="img" aria-label="Close-up photo of a child's sandy bare feet">
        <defs>
          <linearGradient id="feetBase" x1="0" y1="0" x2="1" y2="1">
            <stop offset="0" stop-color="#b98f88"/>
            <stop offset=".5" stop-color="var(--skin-pink)"/>
            <stop offset="1" stop-color="#a9807a"/>
          </linearGradient>
          <radialGradient id="footGlow" cx=".5" cy=".5" r=".5">
            <stop offset="0" stop-color="var(--skin-light)"/>
            <stop offset=".6" stop-color="#dbb7ae" stop-opacity=".7"/>
            <stop offset="1" stop-color="#dbb7ae" stop-opacity="0"/>
          </radialGradient>
          <radialGradient id="sandGlow" cx=".5" cy=".5" r=".5">
            <stop offset="0" stop-color="var(--sand)" stop-opacity=".95"/>
            <stop offset="1" stop-color="var(--sand)" stop-opacity="0"/>
          </radialGradient>
        </defs>
        <rect width="520" height="292" fill="url(#feetBase)"/>
        <ellipse cx="140" cy="150" rx="170" ry="120" fill="url(#footGlow)"/>
        <ellipse cx="330" cy="90" rx="130" ry="90" fill="url(#footGlow)"/>
        <ellipse cx="250" cy="80" rx="70" ry="40" fill="url(#sandGlow)"/>
        <ellipse cx="95" cy="215" rx="80" ry="40" fill="url(#sandGlow)"/>
        <polygon points="430,0 520,0 520,292 225,292" fill="var(--sky-blue)" opacity=".92"/>
      </svg>
      <div class="feature-copy">
        <h1 class="feature-title">WE FIX FEET!</h1>
        <p class="feature-text">Marlow Stride Clinic is very proud to be recognise as one of perth's leading Family and Sports Podiatry practices</p>
      </div>
    </section>

    <div class="divider"></div>

    <section class="kids">
      <svg viewBox="0 0 520 262" preserveAspectRatio="none" role="img" aria-label="Photo of happy children sitting barefoot on grass">
        <defs>
          <linearGradient id="kidsSky" x1="0" y1="0" x2="0" y2="1">
            <stop offset="0" stop-color="var(--sky)"/>
            <stop offset=".7" stop-color="#dfe9ec"/>
            <stop offset=".75" stop-color="var(--grass)"/>
            <stop offset="1" stop-color="#4f8a26"/>
          </linearGradient>
          <linearGradient id="shirtBand" x1="0" y1="0" x2="1" y2="0">
            <stop offset="0" stop-color="#b07a52"/>
            <stop offset=".3" stop-color="#d98f9a"/>
            <stop offset=".42" stop-color="var(--shirt-green)"/>
            <stop offset=".58" stop-color="#f4e7d0"/>
            <stop offset=".7" stop-color="var(--shirt-red)"/>
            <stop offset=".88" stop-color="var(--shirt-yellow)"/>
            <stop offset="1" stop-color="#eef2d0"/>
          </linearGradient>
          <linearGradient id="legBand" x1="0" y1="0" x2="1" y2="0">
            <stop offset="0" stop-color="#d9a57c"/>
            <stop offset=".5" stop-color="#8e8a86"/>
            <stop offset="1" stop-color="#e2b894"/>
          </linearGradient>
          <linearGradient id="skinBand" x1="0" y1="0" x2="1" y2="0">
            <stop offset="0" stop-color="#e8b48f"/>
            <stop offset="1" stop-color="#f0c6a2"/>
          </linearGradient>
          <filter id="soften" x="-10%" y="-30%" width="120%" height="160%">
            <feGaussianBlur stdDeviation="9"/>
          </filter>
        </defs>
        <rect width="520" height="262" fill="url(#kidsSky)"/>
        <g filter="url(#soften)">
          <rect x="10" y="30" width="510" height="50" rx="25" fill="url(#skinBand)" opacity=".85"/>
          <rect x="0" y="80" width="520" height="75" rx="20" fill="url(#shirtBand)"/>
          <rect x="20" y="150" width="500" height="45" rx="20" fill="url(#legBand)" opacity=".9"/>
          <rect x="60" y="190" width="460" height="40" rx="20" fill="url(#skinBand)" opacity=".8"/>
        </g>
        <polygon points="0,0 110,0 245,262 0,262" fill="var(--warm-orange)" opacity=".82"/>
      </svg>
      <p class="kids-copy">visit our website at:<br>www.marlowstrideclinic.net<br>to get more info</p>
    </section>

    <footer class="contact">
      <span class="contact-item">
        <svg width="30" height="30" viewBox="0 0 30 30" aria-hidden="true">
          <circle cx="15" cy="15" r="15" fill="var(--brand-blue)"/>
          <path d="M10 8c1-1 2-1 3 0l1.5 2.5c.4.8.2 1.5-.5 2l-1 .8c.8 1.8 2 3 3.7 3.8l.8-1c.5-.7 1.2-.9 2-.5L22 17c1 .6 1 1.8 0 2.8-1.6 1.6-4 1.5-7-1-2.7-2.4-4.5-5.2-5-7.5-.3-1.4.2-2.5 0-3.3z" fill="var(--white)"/>
        </svg>
        08 7261 8092
      </span>
      <span class="contact-item">
        <svg width="32" height="28" viewBox="0 0 32 28" aria-hidden="true">
          <rect x="8" y="1" width="16" height="10" fill="none" stroke="var(--brand-blue)" stroke-width="2"/>
          <rect x="1" y="9" width="30" height="18" rx="2" fill="var(--brand-blue)"/>
          <rect x="4" y="13" width="5" height="11" fill="var(--white)"/>
          <rect x="12" y="13" width="16" height="3" fill="var(--white)"/>
        </svg>
        08 7261 8093
      </span>
      <span class="contact-item">
        <svg width="32" height="22" viewBox="0 0 32 22" aria-hidden="true">
          <rect x="1" y="1" width="30" height="20" fill="var(--brand-blue)"/>
          <path d="M1 1l15 11L31 1M1 21l11-10M31 21L20 11" fill="none" stroke="var(--white)" stroke-width="1.6"/>
        </svg>
        info@marlowstrideclinic.net
      </span>
    </footer>
  </main>
</body>
</html>
```